A-Stand Directional Sign Design

Objective:
We need a professional graphic design for an A-Stand sign that will guide customers arriving in our parking lot to our office. The design should be visually clear, welcoming, and aligned with our brand identity.
REQUIREMENTS:
Two versions of the design:
- One with an arrow pointing left
- One with an arrow pointing right
(This allows us to place the A-Stand anywhere and flip the graphic as needed.)
DIMENSIONS:
- Viewable Area: 30" x 40"
BRAND ALIGNMENT:
- Colors, fonts, and overall style should match our website: www.glidecrest.com
- Clean, modern, and professional look consistent with our aviation/tourism brand
CONTENT:
- Clear directional arrow (left or right depending on version)
- Text: “Office Entrance” or similar concise wording (designers may propose alternatives if they improve clarity)
READABILITY:
- Bold, high-contrast design for visibility from a distance
- Simple layout that avoids clutter
DELIVERABLES:
- Final artwork in print-ready format (PDF preferred)
- Two versions: Arrow Left and Arrow Right
DESIGN GOAL:
Ensure customers can easily find our office upon arrival, while reinforcing glideCREST’s professional and welcoming brand image.
Target Market(s)
Tourism
Look and feel

```html
<!DOCTYPE html>
<html lang="en">
<head>
<meta charset="utf-8">
<title>glideCREST – Office Entrance A-Stand Sign</title>
<link href="https://fonts.googleapis.com/css2?family=Fira+Sans+Extra+Condensed:wght@200;600&display=swap" rel="stylesheet">
<style>
  :root {
    --page-bg: #ffffff;
    --sea-top: #1b72ad;
    --sea-mid: #17609a;
    --sea-deep: #0c3a62;
    --ink-light: #ffffff;
    --arrow-blue: #145f97;
  }
  html, body {
    margin: 0;
    padding: 0;
    width: 1075px;
    height: 1200px;
    overflow: hidden;
    background: var(--page-bg);
  }
  .canvas {
    position: relative;
    width: 1075px;
    height: 1200px;
  }
  .sign {
    position: absolute;
    left: 257px;
    top: 40px;
    width: 560px;
    height: 1120px;
    overflow: hidden;
    box-shadow: 0 6px 24px rgba(0,0,0,0.18);
  }
  .sign-backdrop {
    position: absolute;
    inset: 0;
    background:
      radial-gradient(ellipse at 50% 85%, rgba(12,58,98,0.0) 0%, rgba(12,58,98,0.35) 70%),
      linear-gradient(180deg, var(--sea-top) 0%, var(--sea-mid) 40%, var(--sea-deep) 100%);
  }
  .sign-content {
    position: absolute;
    inset: 0;
    color: var(--ink-light);
    font-family: "Fira Sans Extra Condensed", "Arial Narrow", sans-serif;
  }
  .brand {
    position: absolute;
    top: 212px;
    left: 0;
    right: 0;
    display: flex;
    flex-direction: column;
    align-items: center;
  }
  .brand-name {
    font-weight: 600;
    font-size: 46px;
    letter-spacing: 1px;
    line-height: 1;
  }
  .brand-rule {
    width: 200px;
    height: 3px;
    margin-top: 14px;
    background: var(--ink-light);
  }
  .headline {
    position: absolute;
    top: 350px;
    left: 0;
    right: 0;
    margin: 0;
    font-weight: 200;
    font-size: 108px;
    line-height: 1.1;
    text-align: center;
    letter-spacing: -3px;
  }
  .direction-arrow {
    position: absolute;
    top: 640px;
    left: 120px;
    width: 320px;
    height: 320px;
  }
</style>
</head>
<body>
<main class="canvas">
  <section class="sign">
    <div class="sign-backdrop" role="img" aria-label="Dusky blue ocean photo with a helicopter silhouette resting near the lower right"></div>
    <div class="sign-content">
      <header class="brand">
        <span class="brand-name">glideCREST</span>
        <span class="brand-rule"></span>
      </header>
      <h1 class="headline">Office<br>Entrance</h1>
      <svg class="direction-arrow" viewBox="0 0 300 300" aria-label="Arrow pointing right">
        <circle cx="150" cy="150" r="150" fill="var(--ink-light)"/>
        <polygon points="60,125 140,125 112,72 160,72 222,150 160,228 112,228 140,175 60,175" fill="var(--arrow-blue)"/>
      </svg>
    </div>
  </section>
</main>
</body>
</html>
```